Construction Company Business Card

Business Card Design using new Logo

Contact Information for Business Card

include all company info and website

Requirements
Must have
• Wesley Corman - President
ph. 254-617-0382
Cedar Knoll, TX
wesley@ironmarkframing.com
www.ironmarkframing.com

```html
<!DOCTYPE html>
<html lang="en">
<head>
<meta charset="utf-8">
<title>Ironmark Framing – Business Card</title>
<link rel="stylesheet" href="https://fonts.googleapis.com/css2?family=Montserrat:wght@400;500;600;700&display=swap">
<style>
  :root {
    --brand-red: #b71f25;
    --brand-grey: #9c9c9c;
    --ink: #3a3a3a;
    --paper: #ffffff;
    --table: #e4e8e9;
  }
  * { box-sizing: border-box; margin: 0; padding: 0; }
  html, body { width: 1200px; height: 1200px; overflow: hidden; }
  body {
    position: relative;
    background: var(--paper);
    font-family: "Montserrat", sans-serif;
  }
  .brand-header {
    position: absolute; top: 0; left: 0;
    width: 1200px; height: 292px;
    display: flex; align-items: center; justify-content: center;
  }
  .wordmark {
    display: flex; align-items: center; gap: 12px;
  }
  .wordmark-square {
    width: 14px; height: 14px; background: var(--brand-red);
  }
  .wordmark-name {
    font-weight: 500; letter-spacing: 2px;
    color: var(--brand-grey); text-transform: uppercase;
  }
  .brand-header .wordmark-name { font-size: 22px; }

  .card-table {
    position: absolute; top: 292px; left: 0;
    width: 1200px; height: 908px;
    background: var(--table);
  }
  .card {
    position: absolute; left: 240px;
    width: 720px; height: 400px;
    background: var(--paper);
    overflow: hidden;
    box-shadow: 0 3px 0 #d2d6d7, 0 12px 26px rgba(0,0,0,0.12);
  }
  .card-front { top: 36px; }
  .card-back { top: 472px; }

  .card-band {
    position: absolute; left: 0; width: 100%;
    background: var(--brand-red);
  }
  .card-front .card-band { top: 160px; height: 80px; }
  .logo-disc {
    position: absolute; left: 230px; top: 70px;
    width: 260px; height: 260px; border-radius: 50%;
    background: var(--paper);
    box-shadow: 0 6px 18px rgba(0,0,0,0.22);
    display: flex; align-items: center; justify-content: center;
  }
  .logo-disc .wordmark-name { font-size: 17px; }
  .logo-disc .wordmark-square { width: 11px; height: 11px; }

  .card-back .card-band {
    top: 96px; height: 86px;
    padding: 14px 0 0 64px; color: var(--paper);
  }
  .holder-name { font-size: 30px; font-weight: 700; letter-spacing: 1px; text-transform: uppercase; line-height: 1.1; }
  .holder-title { font-size: 16px; font-weight: 600; letter-spacing: 1.5px; text-transform: uppercase; margin-left: 100px; }

  .contact-list {
    position: absolute; left: 64px; top: 222px;
    list-style: none; color: var(--ink);
    font-size: 17px; line-height: 30px;
  }
  .contact-list li { display: flex; align-items: center; gap: 12px; }
  .contact-icon { width: 16px; height: 16px; fill: var(--brand-red); flex: none; }
</style>
</head>
<body>
  <header class="brand-header">
    <div class="wordmark">
      <span class="wordmark-square"></span>
      <span class="wordmark-name">Ironmark Framing</span>
    </div>
  </header>

  <main class="card-table">
    <section class="card card-front" aria-label="Card front">
      <div class="card-band"></div>
      <div class="logo-disc">
        <div class="wordmark">
          <span class="wordmark-square"></span>
          <span class="wordmark-name">Ironmark Framing</span>
        </div>
      </div>
    </section>

    <section class="card card-back" aria-label="Card back">
      <div class="card-band">
        <div class="holder-name">Wesley Corman</div>
        <div class="holder-title">President</div>
      </div>
      <ul class="contact-list">
        <li>
          <svg class="contact-icon" viewBox="0 0 16 16"><path d="M4 1l3 3-2 2c1 2 3 4 5 5l2-2 3 3-2 3C7 15 1 9 1 3z"/></svg>
          254-617-0382
        </li>
        <li>
          <svg class="contact-icon" viewBox="0 0 16 16"><path d="M8 1a5 5 0 0 0-5 5c0 4 5 9 5 9s5-5 5-9a5 5 0 0 0-5-5zm0 7a2 2 0 1 1 0-4 2 2 0 0 1 0 4z"/></svg>
          Cedar Knoll, TX
        </li>
        <li>
          <svg class="contact-icon" viewBox="0 0 16 16"><path d="M1 3h14v10H1zm1 1v.5l6 4 6-4V4z"/></svg>
          wesley@ironmarkframing.com
        </li>
        <li>
          <svg class="contact-icon" viewBox="0 0 16 16"><path d="M8 1a7 7 0 1 0 0 14A7 7 0 0 0 8 1zm0 2a5 5 0 0 1 4.6 3H3.4A5 5 0 0 1 8 3zm-5 5h10a5 5 0 0 1-10 0z"/></svg>
          www.ironmarkframing.com
        </li>
      </ul>
    </section>
  </main>
</body>
</html>
```